VORNIK Lab Feel your information

VORNIK Lab is a soci% 26 # 233; t% 26 # 233; of mobile application design and multiexperience destiny% 26 # 233; % 26 # 224; The% 26 # 39; industry and particularly the watch industry% 26 # 232; re. By multiexperience, I mean applications usable on watches,% 26 # 233; holographic screens,% 26 # 233; touch screens g% 26 # 233; ant, r% 26 # 233; alit% 26 # 233; virtual,% 26 # 224; distance with a driftgrip and% 26 # 233; obviously on mobile on tablet and smartphone. Applications will call% 26 # 224; 3d, artificial intelligence, big data. The company logo% 26 # 233; t% 26 # 233; is attached% 26 # 233; below.

Target Market(s)

Swiss precision industry Watchmaking industry% 26 # 232; re

Coding

Coded - Design and coding required

Font styles to use
Sans Serif

Colors

Designer to choose colors to be used in the design.

Requirements
Must have
• A Contact form A gallery of Vid% 26 # 233; o / Photo (portfolio) 3D images of% 26 # 39; illustration orient% 26 # 233; es industry but% 26 # 233; also luxury (take free images A partner page
Nice to have
• A blog
Should not have
• The designs are too loaded, the page should load quickly.

```html
<!DOCTYPE html>
<html lang="en">
<head>
<meta charset="utf-8">
<title>VORNIK Lab — Swiss Precision</title>
<link rel="stylesheet" href="https://fonts.googleapis.com/css2?family=Rajdhani:wght@400;500;600&family=Exo+2:wght@400;600&display=swap">
<style>
:root{
  --black:#000;
  --white:#fff;
  --muted:#d4d4d4;
  --field:#dcdcdc;
  --field-text:#6a6a6a;
  --btn-dark:#161616;
  --heading:"Rajdhani",sans-serif;
  --body:"Exo 2",sans-serif;
}
*{box-sizing:border-box;margin:0;padding:0}
html,body{width:1200px;height:4136px;overflow:hidden;background:var(--black)}
body{font-family:var(--body);color:var(--white);position:relative}
a{color:inherit;text-decoration:none}

/* brand */
.brand{display:flex;align-items:center;gap:9px;font-family:var(--heading);font-weight:500;letter-spacing:2px;color:var(--white);font-size:22px;line-height:1}
.brand-square{width:13px;height:13px;background:var(--white)}

/* hero */
.hero{position:absolute;left:0;top:0;width:1200px;height:774px;overflow:hidden;
  background:
    radial-gradient(ellipse 260px 250px at 250px 540px,rgba(70,84,130,.9) 0%,rgba(30,38,70,.85) 60%,transparent 100%),
    radial-gradient(ellipse 520px 260px at 1050px 140px,rgba(150,165,205,.55) 0%,rgba(80,95,145,.25) 55%,transparent 100%),
    radial-gradient(ellipse 420px 520px at 780px 520px,rgba(20,26,52,.85) 0%,transparent 100%),
    linear-gradient(160deg,#26315a 0%,#2b3766 35%,#1a2244 65%,#131a34 100%);}
.hero-shade{position:absolute;inset:0;background:linear-gradient(180deg,rgba(0,0,0,.15) 0%,rgba(0,0,0,0) 40%,rgba(0,0,0,.25) 100%)}
.hero .brand{position:absolute;left:29px;top:42px}
.menu-icon{position:absolute;left:1150px;top:47px}
.hero-title{position:absolute;left:0;width:1200px;top:381px;text-align:center;font-family:var(--heading);font-weight:400;font-size:35px;line-height:31px;letter-spacing:1.5px;text-transform:uppercase}
.hero-cta{position:absolute;left:485px;top:481px;width:225px;height:52px;border:1px solid var(--white);display:flex;align-items:center;justify-content:center;font-family:var(--heading);font-weight:500;font-size:14px;letter-spacing:1px}
.slider-arrow{position:absolute;top:440px}
.slider-arrow.prev{left:27px}
.slider-arrow.next{left:1157px}

/* feature rows */
.feature{position:absolute;left:0;width:1200px;height:600px;display:flex;background:var(--black)}
.feature-text,.feature-media{width:600px;height:600px;position:relative;flex:none}
.feature-text .inner{position:absolute;left:88px;top:166px;width:440px}
.feature-title{font-family:var(--heading);font-weight:500;font-size:22px;letter-spacing:.6px;text-transform:uppercase;line-height:26px}
.feature-sub{font-family:var(--heading);font-weight:600;font-size:13px;text-transform:uppercase;margin-top:1px;letter-spacing:.3px}
.rule{width:72px;height:2px;background:var(--white);margin-top:24px}
.feature-copy{margin-top:30px;width:432px;font-size:14px;line-height:20px;color:var(--muted)}
.feature-copy strong{color:var(--white);font-weight:600}
.actions{display:flex;gap:6px;margin-top:40px}
.btn{width:199px;height:43px;display:flex;align-items:center;justify-content:center;font-family:var(--heading);font-weight:500;font-size:13px;letter-spacing:.5px;text-transform:uppercase}
.btn.outline{border:1px solid var(--white)}
.btn.solid{background:var(--btn-dark)}

.media-globe{background:
  radial-gradient(circle 150px at 300px 310px,rgba(196,160,60,.85) 0%,rgba(120,140,60,.5) 55%,transparent 100%),
  radial-gradient(circle 275px at 300px 245px,rgba(90,190,150,.55) 0%,rgba(40,110,110,.45) 70%,transparent 100%),
  radial-gradient(ellipse at 20% 10%,#3a4e8e 0%,transparent 45%),
  radial-gradient(ellipse at 85% 90%,#4a3a6a 0%,transparent 45%),
  linear-gradient(135deg,#1a2450 0%,#0e1430 50%,#1d1a3a 100%);}
.media-camera{background:
  radial-gradient(ellipse 110px 220px at 228px 345px,#1d55c8 0%,#0e2a78 55%,transparent 100%),
  radial-gradient(ellipse 170px 300px at 228px 330px,#121418 0%,#0a0a0c 80%,transparent 100%),
  radial-gradient(circle 120px at 560px 430px,rgba(230,190,110,.9) 0%,transparent 100%),
  radial-gradient(circle 100px at 510px 120px,rgba(200,220,160,.75) 0%,transparent 100%),
  radial-gradient(circle 110px at 20px 180px,rgba(210,140,50,.85) 0%,transparent 100%),
  radial-gradient(circle 140px at 560px 590px,rgba(220,150,50,.9) 0%,transparent 100%),
  linear-gradient(180deg,#1c1810 0%,#2a2214 60%,#5a3c18 100%);}
.media-castle{background:
  radial-gradient(ellipse 250px 170px at 340px 230px,rgba(190,120,80,.95) 0%,rgba(150,110,80,.5) 60%,transparent 100%),
  radial-gradient(ellipse 330px 140px at 320px 370px,rgba(70,80,40,.95) 0%,transparent 100%),
  linear-gradient(155deg,#8a9aa8 0%,#a4aab2 28%,#9a8a74 48%,#4c5028 62%,#d8c6b2 80%,#a48c78 100%);}
.media-desk{background:
  radial-gradient(ellipse 150px 100px at 370px 250px,#050505 0%,#111 70%,transparent 100%),
  linear-gradient(135deg,transparent 0%,transparent 62%,#cfcfcf 72%,#eaeaea 100%),
  linear-gradient(150deg,#141414 0%,#262626 25%,#3e3e3e 50%,#2a2a2a 100%);}

/* contact */
.contact-form{margin-top:27px;width:308px;display:flex;flex-direction:column;gap:10px}
.field{height:32px;background:var(--field);color:var(--field-text);font-size:11px;padding:0 20px;display:flex;align-items:center;text-transform:uppercase;letter-spacing:.5px}
.field.message{height:82px;align-items:flex-start;padding-top:10px}
.contact-form .btn{margin-top:2px}

/* gallery */
.gallery{position:absolute;left:0;top:3175px;width:1200px;height:695px;display:grid;grid-template-columns:400px 400px 400px;grid-template-rows:232px 232px 231px}
.tile{position:relative}
.tile-1{background:radial-gradient(ellipse 120px 80px at 210px 110px,#6a727c 0%,transparent 100%),linear-gradient(135deg,#3a4656 0%,#1c2430 55%,#2a3038 100%)}
.tile-2{background:radial-gradient(ellipse 110px 90px at 230px 120px,#1a1a1c 0%,transparent 100%),linear-gradient(135deg,#7a7a7e 0%,#5a5a5e 50%,#48484c 100%)}
.tile-3{background:radial-gradient(ellipse 150px 80px at 300px 110px,#8a8a90 0%,transparent 100%),linear-gradient(135deg,#6a5448 0%,#3a322e 50%,#5e5a5c 100%)}
.tile-4{background:radial-gradient(ellipse 50px 90px at 195px 110px,#0c0c0e 0%,transparent 100%),linear-gradient(180deg,#5a5e66 0%,#6a6058 45%,#3a3028 100%)}
.tile-5{background:radial-gradient(ellipse 130px 70px at 220px 100px,#0c0c10 0%,transparent 100%),linear-gradient(135deg,#3a3c42 0%,#24262a 60%,#1a1a1c 100%)}
.tile-6{background:radial-gradient(ellipse 70px 100px at 150px 115px,#203e8a 0%,#0c0e18 80%,transparent 100%),radial-gradient(circle 90px at 360px 160px,rgba(190,130,50,.8) 0%,transparent 100%),linear-gradient(135deg,#1a1810 0%,#141416 60%,#3a2a14 100%)}
.tile-7{background:radial-gradient(circle 100px at 180px 120px,#5a6a2e 0%,#2a4a46 55%,transparent 100%),linear-gradient(135deg,#1a2448 0%,#0e1226 100%)}
.tile-8{background:radial-gradient(ellipse 150px 60px at 200px 200px,#c8b8a8 0%,transparent 100%),radial-gradient(circle 70px at 240px 130px,#8a3a24 0%,transparent 100%),linear-gradient(160deg,#6a7a3a 0%,#7a6a60 45%,#4a4448 100%)}
.tile-9{background:radial-gradient(circle 70px at 200px 80px,#e89a3a 0%,#8a4a18 45%,transparent 100%),linear-gradient(180deg,#2a2620 0%,#1a1a1a 100%)}
.tile-caption{position:absolute;right:20px;bottom:22px;text-align:right;font-family:var(--heading);text-transform:uppercase;line-height:14px}
.tile-caption .name{font-size:17px;letter-spacing:.4px}
.tile-caption .place{font-size:11px;font-weight:500}

/* footer */
.footer{position:absolute;left:0;top:3870px;width:1200px;height:266px;background:var(--black)}
.footer .brand{position:absolute;left:37px;top:112px;font-size:24px}
.copyright{position:absolute;left:37px;top:161px;font-size:13px;font-family:var(--heading);font-weight:500;text-transform:uppercase}
.footer-col{position:absolute;top:84px;font-family:var(--heading);font-size:13px;text-transform:uppercase;line-height:20px}
.footer-col h4{font-weight:600;font-size:13px;margin-bottom:9px}
.footer-col li{list-style:none;font-weight:500}
</style>
</head>
<body>

<header class="hero">
  <div class="hero-shade" role="img" aria-label="Close-up of a hand wearing a round smartwatch in dusky blue light"></div>
  <div class="brand"><span class="brand-square"></span>VORNIK LAB</div>
  <svg class="menu-icon" width="24" height="18" viewBox="0 0 24 18" aria-label="Menu">
    <rect y="1" width="24" height="2.5" fill="#fff"/><rect y="7.5" width="24" height="2.5" fill="#fff"/><rect y="14" width="24" height="2.5" fill="#fff"/>
  </svg>
  <h1 class="hero-title">A new standard<br>of precision and innovation</h1>
  <a class="hero-cta">LEARN MORE</a>
  <svg class="slider-arrow prev" width="18" height="32" viewBox="0 0 18 32"><polyline points="16,2 2,16 16,30" fill="none" stroke="#fff" stroke-width="2"/></svg>
  <svg class="slider-arrow next" width="18" height="32" viewBox="0 0 18 32"><polyline points="2,2 16,16 2,30" fill="none" stroke="#fff" stroke-width="2"/></svg>
</header>

<section class="feature" style="top:774px">
  <div class="feature-text">
    <div class="inner">
      <h2 class="feature-title">About VORNIK Lab</h2>
      <p class="feature-sub">Swiss precision</p>
      <div class="rule"></div>
      <p class="feature-copy">Lorem ipsum dolor sit amet, consectetur adipiscing elit, sed do eiusmod tempor incididunt <strong>ut labore et dolore magna aliqua.</strong> Ut enim ad minim veniam, quis nostrud exercitation ullamco laboris nisi ut aliquip.</p>
      <div class="actions"><a class="btn outline">See prices</a><a class="btn solid">Learn more</a></div>
    </div>
  </div>
  <div class="feature-media media-globe" role="img" aria-label="Earth wrapped in a glowing network of connected points"></div>
</section>

<section class="feature" style="top:1374px">
  <div class="feature-media media-camera" role="img" aria-label="Hand holding a smartphone photographing a city at night with warm bokeh lights"></div>
  <div class="feature-text">
    <div class="inner">
      <h2 class="feature-title">The future is here</h2>
      <p class="feature-sub">Modern approach</p>
      <div class="rule"></div>
      <p class="feature-copy">Lorem ipsum dolor sit amet, consectetur adipiscing elit, sed do eiusmod tempor incididunt <strong>ut labore et dolore magna aliqua.</strong> Ut enim ad minim veniam, quis nostrud exercitation ullamco laboris nisi ut aliquip.</p>
      <div class="actions"><a class="btn solid">Learn more</a></div>
    </div>
  </div>
</section>

<section class="feature" style="top:1974px">
  <div class="feature-text">
    <div class="inner">
      <h2 class="feature-title">Brilliant minds</h2>
      <p class="feature-sub">Great ideas</p>
      <div class="rule"></div>
      <p class="feature-copy">Lorem ipsum dolor sit amet, consectetur adipiscing elit, sed do eiusmod tempor incididunt <strong>ut labore et dolore magna aliqua.</strong> Ut enim ad minim veniam, quis nostrud exercitation ullamco laboris nisi ut aliquip.</p>
      <div class="actions"><a class="btn outline">See prices</a><a class="btn solid">Learn more</a></div>
    </div>
  </div>
  <div class="feature-media media-castle" role="img" aria-label="Castle on a wooded hill rising out of a smartphone screen"></div>
</section>

<section class="feature" style="top:2575px">
  <div class="feature-media media-desk" role="img" aria-label="Desk with notebook, pen, smartphone and laptop corner"></div>
  <div class="feature-text">
    <div class="inner" style="top:151px">
      <h2 class="feature-title">Contact us</h2>
      <p class="feature-sub">We reply very fast</p>
      <div class="rule"></div>
      <form class="contact-form">
        <div class="field">Name</div>
        <div class="field">Email</div>
        <div class="field message">Message</div>
        <a class="btn solid">Learn more</a>
      </form>
    </div>
  </div>
</section>

<section class="gallery" aria-label="Portfolio">
  <div class="tile tile-1" role="img" aria-label="Wrist with a square smartwatch"></div>
  <div class="tile tile-2" role="img" aria-label="Laptop and headphones on a desk"></div>
  <div class="tile tile-3" role="img" aria-label="Hands typing on a laptop"></div>
  <div class="tile tile-4" role="img" aria-label="Phone held up against a beach at dusk"></div>
  <div class="tile tile-5" role="img" aria-label="Hand holding a dark smartphone">
    <div class="tile-caption"><div class="name">Project Nexus 029</div><div class="place">Switzerland, 2020</div></div>
  </div>
  <div class="tile tile-6" role="img" aria-label="Smartphone camera capturing a night skyline"></div>
  <div class="tile tile-7" role="img" aria-label="Earth wrapped in a glowing network"></div>
  <div class="tile tile-8" role="img" aria-label="Finger touching a phone screen"></div>
  <div class="tile tile-9" role="img" aria-label="Glowing light bulb in the dark"></div>
</section>

<footer class="footer">
  <div class="brand"><span class="brand-square"></span>VORNIK LAB</div>
  <p class="copyright">Copyright 2020</p>
  <div class="footer-col" style="left:405px"><h4>Navigation</h4><ul><li>Home</li><li>About</li><li>Contact</li><li>Terms</li></ul></div>
  <div class="footer-col" style="left:737px"><h4>Services</h4><ul><li>Computer</li><li>Mobile phone</li><li>Watches</li><li>Screens</li></ul></div>
  <div class="footer-col" style="left:1070px"><h4>Projects</h4><ul><li>Nexus home</li><li>Shining bulb</li><li>Touch screen</li><li>Global net</li></ul></div>
</footer>

</body>
</html>
```